KAY VELORE

We need a letterhead design for an Image & Etiquette Consultancy company based in Singapore.

The services we provide are Personal Image Consultation, Image & Etiquette Workshop for schools and corporate.

The design should have our corporate colour as seen in the logo files I have uploaded.

Since our company helps clients with their image, the design should be aesthetically very appealing. It should reflect a very classy & elegant feel.

I will print the letterhead using my printer but most of the time will use it to write letters to my clients therefore the format should include MS Word.

```html
<!DOCTYPE html>
<html lang="en">
<head>
<meta charset="utf-8">
<title>Kay Velore Letterhead</title>
<link rel="stylesheet" href="https://fonts.googleapis.com/css2?family=Michroma&display=swap">
<style>
  :root {
    --navy: #170052;
    --silver-edge: #c4c9c9;
    --silver-mid: #eef0f0;
    --paper: #ffffff;
    --gold-dark: #b8901c;
    --gold-light: #f0dc8a;
    --backdrop: #ffffff;
  }
  html, body {
    margin: 0;
    padding: 0;
    width: 1000px;
    height: 1200px;
    overflow: hidden;
    background: var(--backdrop);
  }
  .letterhead {
    position: absolute;
    left: 110px;
    top: 58px;
    width: 760px;
    height: 1072px;
    background: radial-gradient(ellipse 62% 58% at 50% 50%, var(--paper) 55%, var(--silver-mid) 80%, var(--silver-edge) 100%);
    overflow: hidden;
  }
  .header-band {
    position: absolute;
    left: 0;
    top: 0;
    width: 100%;
    height: 107px;
    background: var(--navy);
  }
  .name-band {
    position: absolute;
    left: 0;
    top: 107px;
    width: 100%;
    height: 50px;
    background: linear-gradient(90deg, var(--silver-edge) 0%, var(--silver-mid) 20%, #fafafa 50%, var(--silver-mid) 80%, var(--silver-edge) 100%);
  }
  .name-rule {
    position: absolute;
    left: 0;
    top: 157px;
    width: 100%;
    height: 23px;
    background: var(--navy);
  }
  .company-name {
    position: absolute;
    left: 98px;
    top: 112px;
    margin: 0;
    font-family: "Michroma", sans-serif;
    font-weight: 400;
    font-size: 38px;
    line-height: 44px;
    letter-spacing: 1px;
    color: var(--navy);
  }
  .footer-band {
    position: absolute;
    left: 0;
    bottom: 0;
    width: 760px;
    height: 145px;
  }
</style>
</head>
<body>
  <main class="letterhead">
    <div class="header-band"></div>
    <div class="name-band"></div>
    <h1 class="company-name">KAY VELORE</h1>
    <div class="name-rule"></div>

    <svg class="footer-band" viewBox="0 0 760 145" xmlns="http://www.w3.org/2000/svg" aria-hidden="true">
      <defs>
        <linearGradient id="gold-sweep" x1="0" y1="0" x2="1" y2="0">
          <stop offset="0" stop-color="var(--gold-dark)"/>
          <stop offset="0.45" stop-color="var(--gold-light)"/>
          <stop offset="1" stop-color="var(--gold-dark)"/>
        </linearGradient>
      </defs>
      <path d="M0 4 L760 0 L760 2 L0 14 Z" fill="var(--navy)"/>
      <path d="M0 4 L760 2 L760 4 L0 13 Z" fill="url(#gold-sweep)"/>
      <path d="M0 13 L760 3 L760 145 L0 145 Z" fill="var(--navy)"/>
    </svg>
  </main>
</body>
</html>
```